I have an existing corporate logo. I'd like to clean it up bit (sharpen it up) and make it look better (without major redesign). I'd like to get the logo itself in all major file formats for print, web, etc.
Then I'd like a business card design that reflects a strategy consulting firm. It should be clean - logo and text without major graphics, and perhaps some small color treatments that match the logo color. The card should suggest high quality in terms of the company.
I'd like the files for card in all major print formats.
Target Market(s)
Silver Birch Partners is a strategy development and business consulting firm focused on small to mid-sized companies. We specialize in business strategy, comprehensive business plan development, market segmentation and positioning, financial models, marketing and sales strategy, product strategy and the effective use of social media in business growth. We operate as consultants, advisers, retained members of management teams, and Board members. We often serve in the role of Chief Strategy Officer, supporting CEO's and other senior executives to enhance top and bottom line growth.
Our overall approach with clients is to deliver actual results, and we often take an active team role with business founders and management teams to drive business growth and affect real changes in performance. As a result, we approach each situation uniquely and partner with clients in a manner that will have the biggest impact on enterprise value.
Industry/Entity Type
Business
Look and feel

```html
<!DOCTYPE html>
<html lang="en">
<head>
<meta charset="utf-8">
<title>Silver Birch Partners – Business Card</title>
<link rel="stylesheet" href="https://fonts.googleapis.com/css2?family=Cinzel:wght@600&family=Didact+Gothic&display=swap">
<style>
  :root {
    --navy: #1f3165;
    --ink: #111111;
    --card: #ffffff;
    --backdrop: #e4e5ea;
    --band: #1f3165;
  }
  * { box-sizing: border-box; margin: 0; padding: 0; }
  html, body {
    width: 1200px;
    height: 790px;
    overflow: hidden;
    background: var(--backdrop);
  }
  .canvas {
    position: relative;
    width: 1200px;
    height: 790px;
  }
  .business-card {
    position: absolute;
    left: 100px;
    top: 110px;
    width: 1000px;
    height: 571px;
    background: var(--card);
    box-shadow: 0 6px 24px rgba(0, 0, 0, 0.18);
    overflow: hidden;
  }
  .brand {
    position: absolute;
    left: 48px;
    top: 42px;
    display: flex;
    align-items: center;
    gap: 18px;
  }
  .brand-mark {
    width: 22px;
    height: 22px;
    border-radius: 50%;
    background: var(--navy);
  }
  .brand-name {
    font-family: "Cinzel", serif;
    font-weight: 600;
    font-size: 38px;
    line-height: 1.12;
    letter-spacing: 1px;
    color: var(--navy);
  }
  .contact {
    position: absolute;
    left: 52px;
    top: 228px;
    font-family: "Didact Gothic", sans-serif;
    font-size: 25px;
    line-height: 1.28;
    color: var(--ink);
  }
  .contact-group + .contact-group { margin-top: 20px; }
  .person {
    position: absolute;
    right: 70px;
    top: 262px;
    text-align: right;
  }
  .person-name {
    font-family: "Cinzel", serif;
    font-weight: 600;
    font-size: 33px;
    color: var(--navy);
    letter-spacing: 0.5px;
  }
  .person-title {
    font-family: "Didact Gothic", sans-serif;
    font-size: 22px;
    color: var(--ink);
    margin-right: 30px;
  }
  .base-band {
    position: absolute;
    left: 0;
    bottom: 0;
    width: 1000px;
    height: 18px;
  }
</style>
</head>
<body>
<main class="canvas">
  <article class="business-card">
    <header class="brand">
      <span class="brand-mark"></span>
      <div class="brand-name">Silver Birch<br>Partners, LLC</div>
    </header>

    <section class="contact">
      <div class="contact-group">
        <p>412 Alder Ridge Lane</p>
        <p>Lakewood, Ohio 44107</p>
      </div>
      <div class="contact-group">
        <p>Direct: 555.204.7318</p>
        <p>Email: daniel@sbpartners.com</p>
        <p>Web: sbpartners.com</p>
      </div>
      <div class="contact-group">
        <p>Network: dharlow</p>
        <p>Social: @DanielHarlow</p>
      </div>
    </section>

    <section class="person">
      <p class="person-name">Daniel M. Harlow</p>
      <p class="person-title">Partner / Founder</p>
    </section>

    <svg class="base-band" viewBox="0 0 1000 18" preserveAspectRatio="none" aria-hidden="true">
      <rect width="1000" height="18" fill="var(--band)"/>
    </svg>
  </article>
</main>
</body>
</html>
```